Guaranteed Web Design (Uncoded - PSD layout only) for kids psychologists, minor logo with runner up

Simple psychologist website
Open brief, creative designs encouraged
Site map:
Home
our services
our psychologists
selective mutism
resources
contact

Current website:
http://mindnest4tots.com.au/
Not in love with our logo, or colours etc - open brief
Happy for new font/style/logo for company name - if we choose a logo design from a designer who doesn't win the competition, we will award $50 for the logo and use it in the new website

Website made a few years ago for a sister company that we really like:
http://www.corlewpsychology.com.au/

Clean, credible and warm and friendly look & feel
stock photos OK, designer will be required to hand over any images used in the design as shown in the PSD

Target Market(s)

Adolescents with psychological issues and their families

Industry/Entity Type

Psychology

Number of Pages Required

2 page

Colors

Designer to choose colors to be used in the design.

Requirements
Must have
• One home page - simple with 2 or 3 small areas to tease and attract the user and one template page to suit all the other pages
• We like slides, we want to have 3 slides like corlewpsychology.com.au
• Three slide titles:
• 1. We specialise in many areas, find the right clinical psychologist for your family
• 2. Child Clinical Psychologists in Chatswood and Westmead
• 3. Resources
• Pages structurally similar to
• http://www.corlewpsychology.com.au/
• We like the 'featured' items, which in our case will have splash box titles (can be 3 or 4):
• 1. Selective Mutism
• 2. Is my child anxious?
• 3. Does my child have an eating disorder?
• 4. Parenting adolescents
• Does not need to be a copy of http://www.corlewpsychology.com.au/ and we are willing to accept outside-the-box thinking and design (we in fact encourage it)
• Owner of business wants to highlight Selective Mutism as they have specialists. Consider ways that may make this work.
• Design winner will be based on home page design but winning designer will be required to provide an additional but simpler 'standard' page template design based on the themes used in the winning design.

```html
<!DOCTYPE html>
<html lang="en">
<head>
<meta charset="utf-8">
<title>MINDnest – Child Adolescent &amp; Family Psychology</title>
<link rel="stylesheet" href="https://fonts.googleapis.com/css2?family=Noto+Serif:wght@400&family=Quicksand:wght@400;500;700&display=swap">
<style>
:root{
  --purple:#8a80c4;
  --purple-deep:#7c74b8;
  --sky:#67c1e6;
  --lilac-bg:#f1effd;
  --ink:#1d1d24;
  --muted:#6d6d78;
  --white:#ffffff;
}
*{box-sizing:border-box;margin:0;padding:0}
html,body{width:1200px;height:2195px;overflow:hidden;background:var(--white)}
body{position:relative;font-family:"Quicksand",sans-serif;color:var(--ink)}
.abs{position:absolute}

/* top utility bar */
.utility-bar{left:0;top:0;width:1200px;height:41px;border-bottom:2px solid #d9eef8;background:var(--white)}
.utility-bar::before{content:"";position:absolute;left:0;top:0;width:100%;height:4px;background:linear-gradient(90deg,var(--purple),var(--sky))}
.social-dots{left:149px;top:11px;display:flex;gap:6px}
.social-dots span{width:22px;height:22px;border-radius:50%;background:#d4d4d8}
.utility-links{right:151px;top:16px;display:flex;gap:46px;font-size:10px;letter-spacing:1px;color:var(--sky)}

/* header */
.brand{left:149px;top:56px}
.brand-name{font-weight:400;font-size:38px;letter-spacing:3px;line-height:1;color:var(--ink)}
.brand-tag{font-size:11.5px;margin-top:4px;font-weight:500}
.search{left:714px;top:64px;width:338px;height:38px;border:1.5px solid var(--sky);border-radius:4px;overflow:hidden}
.search span{position:absolute;left:12px;top:13px;font-size:9px;letter-spacing:1px;color:var(--muted)}
.search .go{position:absolute;right:0;top:0;width:38px;height:36px;background:var(--sky)}
.search svg{position:absolute;left:9px;top:8px}

/* nav */
.main-nav{left:0;top:123px;width:1200px;height:41px;background:linear-gradient(90deg,var(--purple),var(--sky));display:flex;align-items:center;padding-left:152px}
.main-nav a{color:var(--white);text-decoration:none;font-size:13px;letter-spacing:2.2px;font-weight:500;margin-right:38px;white-space:nowrap}

/* hero */
.hero{left:0;top:164px;width:1200px;height:410px;background:linear-gradient(100deg,#5b6a9a 0%,#8f7ea8 35%,#a27a98 65%,#6d4a6e 100%);border-bottom:4px solid var(--sky)}
.hero-copy{right:149px;top:108px;width:720px;text-align:right;color:var(--white)}
.hero-copy h1{font-family:"Noto Serif",serif;font-weight:400;font-size:37px;line-height:44px;white-space:nowrap;margin-bottom:8px}
.hero-copy p{font-weight:700;font-size:17.5px;line-height:27px;width:630px;margin-left:auto}
.btn{display:inline-block;background:var(--sky);color:var(--white);border-radius:5px;font-size:17px;font-weight:500;text-align:center;letter-spacing:.5px}
.hero-copy .btn{width:150px;height:38px;line-height:38px;margin-top:14px}

/* sections */
.section-title{font-family:"Noto Serif",serif;font-weight:400;font-size:27px;color:var(--ink)}
.view-all{font-size:17px;color:var(--purple-deep);font-weight:500}
.card-photo{width:256px;height:162px;border-radius:5px}
.card-caption{width:260px;text-align:center;font-size:13.5px;line-height:22px;font-weight:500}

.appointment{left:0;top:960px;width:1200px;height:388px;background:var(--lilac-bg)}
.appointment p{font-size:11.5px;line-height:22px;color:var(--muted);width:440px}

.news-date{font-family:"Noto Serif",serif;font-size:17px;color:var(--sky)}
.news-title{font-family:"Noto Serif",serif;font-size:15px;margin-top:12px}
.news-body{font-size:10.5px;line-height:22px;color:#5b5b66;margin-top:4px}
.news-more{display:flex;gap:3px}
.news-more i{width:5px;height:5px;border-radius:50%;background:var(--sky)}

.cta{left:0;top:1695px;width:1200px;height:383px;background:linear-gradient(160deg,#7d7aa8 0%,#8a84b8 45%,#6f6a9e 100%)}
.cta h2{position:absolute;left:0;width:1200px;top:82px;text-align:center;font-family:"Noto Serif",serif;font-weight:400;font-size:39px;letter-spacing:2px;line-height:46px;color:var(--white)}
.cta .btn{position:absolute;left:473px;top:220px;width:225px;height:45px;line-height:45px}

.site-footer{left:0;top:2078px;width:1200px;height:117px;background:var(--purple)}
.copyright{left:150px;top:53px;font-size:17px;letter-spacing:1.5px;color:#aaa3dc}
.follow{left:800px;top:22px;text-align:center;color:var(--white);font-size:17px}
.follow .dots{display:flex;gap:12px;margin-top:8px}
.follow .dots span{width:36px;height:36px;border-radius:50%;background:#a9a2dc}
</style>
</head>
<body>

<div class="utility-bar abs">
  <div class="social-dots abs"><span></span><span></span><span></span><span></span></div>
  <div class="utility-links abs"><span>handouts</span><span>need help?</span><span>who can refer</span><span>contacts</span></div>
</div>

<header>
  <div class="brand abs">
    <div class="brand-name">MINDnest</div>
    <div class="brand-tag">Child Adolescent &amp; Family psychology</div>
  </div>
  <div class="search abs">
    <span>SEARCH HERE</span>
    <div class="go">
      <svg width="20" height="20" viewBox="0 0 20 20"><circle cx="8" cy="8" r="6" fill="none" stroke="#fff" stroke-width="2"/><line x1="12.5" y1="12.5" x2="18" y2="18" stroke="#fff" stroke-width="2.4" stroke-linecap="round"/></svg>
    </div>
  </div>
</header>

<nav class="main-nav abs">
  <a>HOME</a><a>ABOUT US</a><a>FOR PARENTS</a><a>FOR PROFESSIONALS</a><a>FOR TEENS</a><a>BLOG</a><a>CONTACT US</a>
</nav>

<section class="hero abs" role="img" aria-label="Photo of a child walking hand in hand with two parents, purple overlay">
  <div class="hero-copy abs">
    <h1>Child anxiety: How to help manage it</h1>
    <p>Lorem ipsum dolor sit amet, consectetur adipisicing elit, sed do eiusmod tempor incididunt ut labore et dolore magna aliqua. Ut enim ad minim veniam, quis nostrud exercitation ullamco laboris nisi ut aliquip ex ea commodo consequat.</p>
    <span class="btn">read more</span>
  </div>
</section>

<section class="services">
  <h2 class="section-title abs" style="left:151px;top:622px">Our services</h2>
  <span class="view-all abs" style="left:979px;top:639px">View all</span>

  <div class="card-photo abs" style="left:149px;top:679px;background:linear-gradient(135deg,#8aa070,#e8c8a8 50%,#3aa08a)" role="img" aria-label="Photo of a smiling young boy"></div>
  <div class="card-photo abs" style="left:471px;top:679px;background:linear-gradient(135deg,#7a6a5a,#c65a7a 45%,#3c5a8a)" role="img" aria-label="Photo of a family sitting together with a colourful blanket"></div>
  <div class="card-photo abs" style="left:793px;top:679px;background:linear-gradient(135deg,#2a2a2e,#4a4a50 50%,#222)" role="img" aria-label="Photo of a light bulb on a chalkboard with a drawn thought bubble"></div>

  <p class="card-caption abs" style="left:147px;top:867px">Individual counselling and therapy for kids,teens and families</p>
  <p class="card-caption abs" style="left:469px;top:867px">Families consultations</p>
  <p class="card-caption abs" style="left:791px;top:868px">Training and seminars with schools</p>
</section>

<section class="appointment abs">
  <h2 class="section-title abs" style="left:147px;top:76px">Making an appointment</h2>
  <p class="abs" style="left:149px;top:124px">Lorem ipsum dolor sit amet, consectetur adipisicing elit, sed do eiusmod tempor incididunt ut labore et dolore magna aliqua. Ut enim ad minim veniam, quis nostrud exercitation ullamco laboris nisi laborum.</p>
  <span class="btn abs" style="left:146px;top:213px;width:188px;height:38px;line-height:38px">contact us</span>
  <div class="abs" style="left:607px;top:86px;width:442px;height:215px;border-radius:5px;background:linear-gradient(120deg,#6a6a58,#b07a6a 45%,#7a5a50 70%,#5a5a48)" role="img" aria-label="Photo of a smiling girl lying in grass with yellow flowers in her hair"></div>
</section>

<section class="news">
  <h2 class="section-title abs" style="left:148px;top:1401px">Recent News</h2>
  <span class="view-all abs" style="left:985px;top:1416px">View all</span>

  <div class="abs" style="left:151px;top:1457px;width:215px">
    <div class="news-date">03 sept 2017</div>
    <div class="news-title">Selected mutism in children</div>
    <p class="news-body">Lorem ipsum dolor sit amet, consectetur adipiscing elit. Pellentesque volutpat sapien odio, vel tincidunt felis varius in. Maecenas non purus sodales, dignissim elit non, molestie ipsum.</p>
  </div>
  <div class="abs" style="left:471px;top:1457px;width:250px">
    <div class="news-date">04 sept 2017</div>
    <div class="news-title">Selected mutism in children</div>
    <p class="news-body">Fusce tempus sed justo ut semper. In magna eros, facilisis sit amet ligula ut, semper viverra massa. Ut interdum ac ex sit amet placerat. Donec maximus blandit rhoncus.</p>
  </div>
  <div class="abs" style="left:804px;top:1457px;width:250px">
    <div class="news-date">08 sept 2017</div>
    <div class="news-title">Selected mutism in children</div>
    <p class="news-body">Phasellus ut urna orci. Etiam elementum faucibus orci vel finibus. In id erat vitae orci tempor faucibus in sed nulla. Phasellus eget scelerisque est, id posuere urna. In hac habitasse platea dictumst.</p>
  </div>
  <div class="news-more abs" style="left:151px;top:1637px"><i></i><i></i><i></i></div>
  <div class="news-more abs" style="left:471px;top:1637px"><i></i><i></i><i></i></div>
  <div class="news-more abs" style="left:804px;top:1637px"><i></i><i></i><i></i></div>
</section>

<section class="cta abs" role="img" aria-label="Photo of a young couple embracing, seen from behind, purple overlay">
  <h2>Friendly atmosphere<br>for all of your thoughts</h2>
  <span class="btn">subscribe now</span>
</section>

<footer class="site-footer abs">
  <div class="copyright abs">All right reserved | 2017</div>
  <div class="follow abs">
    <div>Follow us</div>
    <div class="dots"><span></span><span></span><span></span><span></span></div>
  </div>
</footer>

</body>
</html>
```